Elk R Cellars Wine Label Design

We are looking to redesign our wine labels. i have updated this contest to focus on just the premium wines. These should have gold writing on a silk screened bottle, or on black traditional label. Red or gold capsule.
Our logo is of a mountain with dated cursive script (see attached). We are hoping to maintain some of that brand identity but with a more premium look. The current cursive script definitely needs to be altered. Elk Ridge is an extinct volcano that is a local landmark in the Okanagan Valley. One concept was using this image as a background or element of the labels or a new logo. i have attached an actual photo of the mountain. This is only to inspire a simplified logo.

Target Market(s)

30-65

Logo Text

Elk. (or Elk) Ravensworth

Font styles to use
Serif
Script

Colors
1b1b1b
ec1f27
fbf289

Requirements
Must have
• High End Feel. silkscreen? gold writing. wine is called "Lantern"
Nice to have
• "estate grown"

```html
<!DOCTYPE html>
<html lang="en">
<head>
<meta charset="utf-8">
<title>Lantern – Elk Ravensworth Estate Grown Label</title>
<link rel="stylesheet" href="https://fonts.googleapis.com/css2?family=Cinzel:wght@500&family=Cormorant+Garamond:wght@500;700&family=Montserrat:wght@700&display=swap">
<style>
  :root {
    --gold: #b5a160;
    --red: #c1272d;
    --black: #000000;
    --paper: #ffffff;
  }
  html, body {
    margin: 0;
    padding: 0;
    overflow: hidden;
  }
  body {
    width: 1200px;
    height: 900px;
    background: var(--paper);
    position: relative;
  }
  .label {
    position: absolute;
    left: 120px;
    top: 147px;
    width: 425px;
    height: 606px;
    background: var(--black);
  }
  .label-frame {
    position: absolute;
    inset: 8px 8px 9px 8px;
    border: 2px solid var(--gold);
  }
  .wine-name {
    position: absolute;
    top: 42px;
    left: 0;
    right: 0;
    margin: 0;
    text-align: center;
    font-family: "Cinzel", "Times New Roman", serif;
    font-weight: 500;
    font-size: 64px;
    letter-spacing: 3px;
    line-height: 1;
    color: var(--gold);
  }
  .estate-name {
    position: absolute;
    top: 338px;
    left: 0;
    right: 0;
    margin: 0;
    text-align: center;
    font-family: "Cormorant Garamond", "Times New Roman", serif;
    font-weight: 500;
    font-size: 44px;
    line-height: 1;
    color: var(--red);
  }
  .estate-grown {
    position: absolute;
    top: 442px;
    left: 0;
    right: 0;
    margin: 0;
    text-align: center;
    font-family: "Cormorant Garamond", "Times New Roman", serif;
    font-weight: 700;
    font-size: 31px;
    letter-spacing: 0.5px;
    line-height: 1;
    color: var(--gold);
  }
  .appellation {
    position: absolute;
    top: 533px;
    left: 0;
    right: 0;
    margin: 0;
    text-align: center;
    font-family: "Cormorant Garamond", "Times New Roman", serif;
    font-weight: 700;
    font-size: 19px;
    letter-spacing: 0.5px;
    line-height: 1;
    color: var(--red);
  }
  .palette {
    position: absolute;
    left: 1123px;
    top: 28px;
    width: 48px;
    margin: 0;
    padding: 0;
    list-style: none;
  }
  .swatch {
    margin-bottom: 15px;
    text-align: center;
    font-family: "Montserrat", Arial, sans-serif;
    font-weight: 700;
    font-size: 9.5px;
    line-height: 11px;
    color: #1b1b1b;
    white-space: nowrap;
  }
  .swatch-chip {
    display: block;
    width: 48px;
    height: 48px;
    margin-bottom: 4px;
  }
  .swatch-gold .swatch-chip { background: var(--gold); }
  .swatch-red .swatch-chip { background: var(--red); }
  .swatch-black .swatch-chip { background: var(--black); }
</style>
</head>
<body>
  <section class="label" aria-label="Lantern wine label">
    <div class="label-frame"></div>
    <h1 class="wine-name">LANTERN</h1>
    <p class="estate-name">Elk Ravensworth</p>
    <p class="estate-grown">ESTATE GROWN</p>
    <p class="appellation">BRITISH COLUMBIA VQA</p>
  </section>

  <ul class="palette" aria-label="Colour palette">
    <li class="swatch swatch-gold"><span class="swatch-chip"></span>GOLD<br>Pantone<br>10119c</li>
    <li class="swatch swatch-red"><span class="swatch-chip"></span>RED<br>C:16, M:100<br>Y:100, K:8</li>
    <li class="swatch swatch-black"><span class="swatch-chip"></span>BLACK<br>C:0, M:0<br>Y:0, K:100</li>
  </ul>
</body>
</html>
```